Design of an attractive membership brochure/membership card for an Electrical Business

Hi, we are an electrical business based in Sydney, Australia.

Our design's aim is to attract and target new customers into using our business as a repeat for anything electrical in their home. We would be handing this out to them after a job is completed and they're happy with the service.
We're thinking of a brochure, possibly additional membership cards with personalized number ID's for each client.

Open to ideas, but some of the things we want to include on our brochure are perks of why the client should sign up with us as a lifetime client
- Discounted emergency call out fees outside of normal hours
- Lifetime membership price, one time payment
- Exclusive 10% member discount on all future jobs
- Priority on any during business hour jobs or emergencies

If any other questions please don't hesitate to reach out.
We've attached our logo for reference for the mock designs.
Our website
https://brightwirecrew.com.au/

```html
<!DOCTYPE html>
<html lang="en">
<head>
<meta charset="utf-8">
<title>Bright Wire Crew – Membership Brochure</title>
<link href="https://fonts.googleapis.com/css2?family=Montserrat:wght@400;500;600;700;800&display=swap" rel="stylesheet">
<style>
  :root {
    --page-bg: #efefef;
    --charcoal: #2b2b2c;
    --charcoal-deep: #1f1f20;
    --paper: #f7f7f7;
    --ink: #1d1d1d;
    --red: #d6383a;
    --white: #ffffff;
    --fold: #d8d8d8;
  }
  * { box-sizing: border-box; margin: 0; padding: 0; }
  html, body {
    width: 1200px; height: 800px; overflow: hidden;
    background: var(--page-bg);
    font-family: "Montserrat", sans-serif;
  }
  .brochure {
    position: absolute; left: 75px; top: 25px;
    width: 1050px; height: 750px;
    display: flex;
    box-shadow: 0 10px 30px rgba(0,0,0,0.12);
  }
  .panel { position: relative; width: 350px; height: 750px; overflow: hidden; flex: none; }

  .panel-title { font-weight: 700; font-size: 25px; line-height: 20px; color: var(--white); }
  .panel-title .accent { color: var(--red); display: block; }

  /* About */
  .panel--about { background: var(--paper); }
  .about-header { height: 125px; background: var(--charcoal); padding: 62px 0 0 46px; }
  .about-text {
    padding: 22px 42px 0 42px;
    font-size: 11.2px; line-height: 16.6px; color: var(--ink);
    text-align: justify; font-weight: 500;
  }
  .about-text p + p { margin-top: 16px; }
  .about-photo { position: absolute; left: -55px; top: 470px; width: 400px; height: 400px; }

  /* Services */
  .panel--services { background: var(--charcoal-deep); box-shadow: inset 1px 0 0 var(--fold), inset -1px 0 0 var(--fold); }
  .services-shape { position: absolute; left: 0; top: 0; width: 350px; height: 750px; }
  .services-header { position: absolute; left: 50px; top: 62px; }
  .service-list { position: absolute; left: 44px; top: 148px; list-style: none; }
  .service {
    display: flex; align-items: center; height: 46px; margin-bottom: 21px;
    font-size: 11.5px; font-weight: 600; line-height: 13px; color: var(--ink); text-transform: uppercase;
  }
  .service-icon {
    width: 46px; height: 46px; border-radius: 9px; background: var(--red);
    margin-right: 12px; flex: none; display: flex; align-items: center; justify-content: center;
  }
  .service-icon svg { width: 30px; height: 30px; fill: none; stroke: var(--white); stroke-width: 1.8; stroke-linecap: round; stroke-linejoin: round; }
  .call-rule { position: absolute; left: 44px; top: 622px; width: 90px; height: 4px; border-radius: 2px; background: var(--red); }
  .call-label { position: absolute; left: 44px; top: 650px; font-size: 15px; font-weight: 600; color: var(--ink); }
  .call-number { position: absolute; left: 44px; top: 672px; font-size: 22px; font-weight: 800; color: var(--ink); }

  /* Membership */
  .panel--membership { background: var(--charcoal); text-align: center; color: var(--white); }
  .membership-photo { position: absolute; left: 38px; top: 55px; width: 268px; height: 252px; }
  .membership-title {
    position: absolute; left: 0; right: 0; top: 345px;
    font-size: 25px; font-weight: 700; line-height: 22px;
  }
  .membership-title .accent { color: var(--red); display: block; }
  .membership-text {
    position: absolute; left: 40px; right: 40px; top: 432px;
    font-size: 11.5px; line-height: 14.6px; font-weight: 500;
  }
  .membership-text p + p { margin-top: 15px; }
</style>
</head>
<body>
<main class="brochure">

  <section class="panel panel--about">
    <header class="about-header">
      <h2 class="panel-title">About<span class="accent">Company</span></h2>
    </header>
    <div class="about-text">
      <p>Bright Wire Crew is a Sydney-based electrical business specialising in electrical maintenance work for residential, commercial, strata and real estate clients. It began with two mates with a strong desire to change the image of tradies and provide exceptional service. As a team of electricians based in the Inner West of Sydney, we understand the need of everyday people struggling to find good, reliable and trustworthy electricians.</p>
      <p>At Bright Wire Crew, we have high expectations of ourselves and strive to improve every day. We're always available around the clock to provide professional advice or give a helping hand when in need.</p>
    </div>
    <svg class="about-photo" viewBox="0 0 400 400">
      <defs>
        <radialGradient id="livingRoomTone" cx="0.5" cy="0.35" r="0.7">
          <stop offset="0" stop-color="#f3d9a0"/>
          <stop offset="0.5" stop-color="#b9833f"/>
          <stop offset="1" stop-color="#4e3a22"/>
        </radialGradient>
      </defs>
      <circle cx="200" cy="200" r="200" fill="var(--charcoal)"/>
      <circle cx="200" cy="212" r="178" fill="url(#livingRoomTone)" role="img" aria-label="Photo of a warmly lit living room with a floor lamp, plant and cushions"/>
    </svg>
  </section>

  <section class="panel panel--services">
    <svg class="services-shape" viewBox="0 0 350 750" preserveAspectRatio="none">
      <path d="M1 125 H190 A159 159 0 0 1 349 284 V750 H1 Z" fill="var(--paper)"/>
    </svg>
    <h2 class="panel-title services-header">Our<span class="accent">Services</span></h2>
    <ul class="service-list">
      <li class="service">
        <span class="service-icon"><svg viewBox="0 0 30 30"><path d="M15 4v5"/><path d="M11 13l4-4 4 4v5a4 4 0 0 1-8 0z"/><path d="M6 22l-2 2M24 22l2 2M15 25v2"/></svg></span>
        Lighting layout design<br>and installations
      </li>
      <li class="service">
        <span class="service-icon"><svg viewBox="0 0 30 30"><path d="M17 4l-8 13h6l-2 9 8-13h-6z"/></svg></span>
        Emergency services
      </li>
      <li class="service">
        <span class="service-icon"><svg viewBox="0 0 30 30"><rect x="5" y="5" width="20" height="20" rx="3"/><path d="M10 10l-1.5 3M20 10l1.5 3M15 17v4"/></svg></span>
        Powerpoint installations<br>or repair
      </li>
      <li class="service">
        <span class="service-icon"><svg viewBox="0 0 30 30"><path d="M5 7h20M7 7v4h16V7"/><path d="M10 15c-1 2 1 3 0 5M15 15c-1 2 1 3 0 5M20 15c-1 2 1 3 0 5"/></svg></span>
        Smoke alarm installations<br>and testing
      </li>
      <li class="service">
        <span class="service-icon"><svg viewBox="0 0 30 30"><rect x="4" y="5" width="22" height="21" rx="1"/><path d="M9 14l6-5 6 5M8 24v-6h4v6M18 18h4v4h-4z"/></svg></span>
        Real estate, strata and<br>commercial
      </li>
      <li class="service">
        <span class="service-icon"><svg viewBox="0 0 30 30"><rect x="4" y="7" width="22" height="16" rx="2"/><path d="M8 12h8M8 16h8M8 20v1M12 20v1M16 20v1"/><circle cx="21" cy="14" r="2"/></svg></span>
        Switchboard upgrade<br>and repairs
      </li>
      <li class="service">
        <span class="service-icon"><svg viewBox="0 0 30 30"><path d="M5 19v-4l3-6h14l3 6v4z"/><path d="M5 15h20"/><circle cx="9.5" cy="17" r="1"/><circle cx="20.5" cy="17" r="1"/><path d="M7 19v3M23 19v3"/></svg></span>
        EV electric vehicle<br>charging stations
      </li>
    </ul>
    <div class="call-rule"></div>
    <p class="call-label">CALL US NOW</p>
    <p class="call-number">0400-317-582</p>
  </section>

  <section class="panel panel--membership">
    <svg class="membership-photo" viewBox="0 0 268 252">
      <defs>
        <linearGradient id="kitchenTone" x1="0" y1="0" x2="0.6" y2="1">
          <stop offset="0" stop-color="#6b5a45"/>
          <stop offset="0.45" stop-color="#3b3937"/>
          <stop offset="1" stop-color="#222223"/>
        </linearGradient>
        <clipPath id="kitchenClip"><rect width="268" height="252"/></clipPath>
      </defs>
      <circle cx="134" cy="134" r="134" fill="url(#kitchenTone)" clip-path="url(#kitchenClip)" role="img" aria-label="Photo of a dark modern kitchen with an island bench and a glowing lamp"/>
    </svg>
    <h2 class="membership-title">Join Our<span class="accent">Membership<br>Program</span></h2>
    <div class="membership-text">
      <p>Searching for a reliable, trusted electrician on call around-the-clock? Look no further than the Always On Electrician Membership from Bright Wire Crew.</p>
      <p>As a member, you'll gain priority service and discounts from our team of fully licensed, experienced electricians based in Sydney. We know electrical emergencies can happen at any time - day or night. That's why with the Always On Membership, you'll receive discounted emergency call-out fees for our after-hours service. No more worrying about expensive bills just to get your electrical issue resolved promptly!</p>
    </div>
  </section>

</main>
</body>
</html>
```